Revise / change slightly the wrap, box and label design. Minor changes only.

We're looking to make some slight changes in positioning and text / colours on our previous packaging. All descriptions will be detailed.

```html
<!DOCTYPE html>
<html lang="en">
<head>
<meta charset="utf-8">
<title>Leafwell Cleaner Labels</title>
<link rel="stylesheet" href="https://fonts.googleapis.com/css2?family=Anton&family=Nunito:wght@400;800&family=Lora:ital@1&display=swap">
<style>
  :root {
    --page: #ffffff;
    --kraft: #d8b98b;
    --kraft-light: #e0c59a;
    --ink: #000000;
    --window: #b5cbe9;
    --window-ink: #7a9cc9;
    --general: #b8e1d3;
    --general-ink: #8cc8ae;
    --kitchen: #f9dbe0;
    --kitchen-ink: #e6a3b1;
    --bathroom: #fcf8c8;
    --bathroom-ink: #e5d58c;
  }
  html, body {
    margin: 0;
    padding: 0;
    overflow: hidden;
    background: var(--page);
  }
  .sheet {
    position: relative;
    width: 1200px;
    height: 535px;
    background: var(--page);
    overflow: hidden;
  }
  .label {
    position: absolute;
    top: 98px;
    width: 245px;
    height: 341px;
    background: var(--tone);
    overflow: hidden;
  }
  .label--window   { left: 67px;  --tone: var(--window);   --accent: var(--window-ink); }
  .label--general  { left: 345px; --tone: var(--general);  --accent: var(--general-ink); }
  .label--kitchen  { left: 622px; --tone: var(--kitchen);  --accent: var(--kitchen-ink); }
  .label--bathroom { left: 900px; --tone: var(--bathroom); --accent: var(--bathroom-ink); }

  .label__kraft {
    position: absolute;
    left: 0; top: 0;
    width: 100%;
    height: 178px;
    background: radial-gradient(ellipse at 40% 30%, var(--kraft-light), var(--kraft));
  }
  .brand {
    position: absolute;
    left: 68px;
    top: 32px;
    display: flex;
    align-items: center;
    gap: 6px;
    font-family: "Nunito", sans-serif;
    font-weight: 800;
    font-size: 24px;
    color: var(--ink);
    letter-spacing: -0.5px;
  }
  .brand__dot {
    width: 12px;
    height: 12px;
    border-radius: 50%;
    background: var(--ink);
  }
  .seal {
    position: absolute;
    left: 132px;
    top: 73px;
    width: 64px;
    height: 64px;
    border: 1.5px solid var(--accent);
    border-radius: 50%;
    box-sizing: border-box;
  }
  .product-type {
    position: absolute;
    left: 53px;
    top: 140px;
    font-family: "Nunito", sans-serif;
    font-weight: 800;
    font-size: 13px;
    color: var(--ink);
    white-space: nowrap;
  }
  .product-name {
    position: absolute;
    left: 52px;
    top: 158px;
    margin: 0;
    font-family: "Anton", sans-serif;
    font-weight: 400;
    font-size: 38px;
    line-height: 38px;
    color: var(--ink);
    letter-spacing: -0.5px;
    white-space: nowrap;
  }
  .tagline {
    position: absolute;
    left: 53px;
    top: 237px;
    font-family: "Lora", serif;
    font-style: italic;
    font-size: 14.5px;
    color: var(--accent);
    white-space: nowrap;
  }
  .origin {
    position: absolute;
    left: 163px;
    top: 286px;
    width: 36px;
    border: 1px solid var(--accent);
    font-family: "Nunito", sans-serif;
    text-align: center;
  }
  .origin__place {
    display: block;
    font-size: 6.5px;
    line-height: 7.5px;
    padding: 2px 0 3px;
    color: var(--accent);
  }
  .origin__place svg { display: block; margin: 0 auto; }
  .origin__volume {
    display: block;
    border-top: 1px solid var(--accent);
    font-size: 9px;
    line-height: 12px;
    color: var(--ink);
  }
  .warning {
    position: absolute;
    left: 225px;
    top: 181px;
    writing-mode: vertical-rl;
    transform: rotate(180deg);
    font-family: "Nunito", sans-serif;
    font-size: 10px;
    line-height: 12px;
    color: var(--accent);
    white-space: nowrap;
  }
</style>
</head>
<body>
<main class="sheet">

  <section class="label label--window">
    <div class="label__kraft"></div>
    <div class="brand"><span>Leafwell</span><span class="brand__dot"></span></div>
    <div class="seal"></div>
    <div class="product-type">Window Cleaner</div>
    <h2 class="product-name">SPARKLE</h2>
    <div class="tagline">Drop In, Clean Up</div>
    <div class="origin">
      <span class="origin__place">Bayside<svg width="20" height="3" viewBox="0 0 20 3"><path d="M1 2 Q10 0 19 1.5" fill="none" stroke="currentColor" stroke-width="0.8"/></svg>Australia</span>
      <span class="origin__volume">500 ml</span>
    </div>
    <div class="warning">Keep out of reach of children</div>
  </section>

  <section class="label label--general">
    <div class="label__kraft"></div>
    <div class="brand"><span>Leafwell</span><span class="brand__dot"></span></div>
    <div class="seal"></div>
    <div class="product-type">Multi Purpose Cleaner</div>
    <h2 class="product-name">THE<br>CAPTAIN</h2>
    <div class="tagline">Drop In, Clean Up</div>
    <div class="origin">
      <span class="origin__place">Bayside<svg width="20" height="3" viewBox="0 0 20 3"><path d="M1 2 Q10 0 19 1.5" fill="none" stroke="currentColor" stroke-width="0.8"/></svg>Australia</span>
      <span class="origin__volume">500 ml</span>
    </div>
    <div class="warning">Keep out of reach of children</div>
  </section>

  <section class="label label--kitchen">
    <div class="label__kraft"></div>
    <div class="brand"><span>Leafwell</span><span class="brand__dot"></span></div>
    <div class="seal"></div>
    <div class="product-type">Kitchen Cleaner</div>
    <h2 class="product-name">GREASE<br>BUSTER</h2>
    <div class="tagline">Drop In, Clean Up</div>
    <div class="origin">
      <span class="origin__place">Bayside<svg width="20" height="3" viewBox="0 0 20 3"><path d="M1 2 Q10 0 19 1.5" fill="none" stroke="currentColor" stroke-width="0.8"/></svg>Australia</span>
      <span class="origin__volume">500 ml</span>
    </div>
    <div class="warning">Keep out of reach of children</div>
  </section>

  <section class="label label--bathroom">
    <div class="label__kraft"></div>
    <div class="brand"><span>Leafwell</span><span class="brand__dot"></span></div>
    <div class="seal"></div>
    <div class="product-type">Bathroom Cleaner</div>
    <h2 class="product-name">THE<br>BLAST</h2>
    <div class="tagline">Drop In, Clean Up</div>
    <div class="origin">
      <span class="origin__place">Bayside<svg width="20" height="3" viewBox="0 0 20 3"><path d="M1 2 Q10 0 19 1.5" fill="none" stroke="currentColor" stroke-width="0.8"/></svg>Australia</span>
      <span class="origin__volume">500 ml</span>
    </div>
    <div class="warning">Keep out of reach of children</div>
  </section>

</main>
</body>
</html>
```